Youth Education Program for WLC

Looking for a high-end slick looking design for power-point and/or PDF. Quick turnaround of a Presentation of 10 slides for a meeting for an educational youth program. Information and recommended images will be provided for each slide. Each Slide other than cover should have a logo, header, footer, and page number. Design should be simple and modern with either graphic examples or images. Less is more. Websites for company is http://brightarcademy.example/ and other images can be found on korvanmedia.example or you can use stock imagery you feel is good.
Colors
Designer to choose colors to be used in the design.
Look and feel
Each slider illustrates characteristics of the customer's brand and the style your logo design should communicate.

```html
<!DOCTYPE html>
<html lang="en">
<head>
<meta charset="utf-8">
<title>Facts — Brightar Academy Youth Program</title>
<link href="https://fonts.googleapis.com/css2?family=Montserrat:wght@600;700&family=Questrial&display=swap" rel="stylesheet">
<style>
  :root {
    --stage: #1c1c1c;
    --green: #8dc63f;
    --grey: #7e7d82;
    --grey-dark: #5d5c61;
    --label-band: #353535;
    --paper: #ffffff;
    --ink-soft: #6f6f73;
    --brand-grey: #9a9a9d;
  }
  html, body {
    margin: 0;
    padding: 0;
    width: 1200px;
    height: 676px;
    overflow: hidden;
    background: var(--stage);
  }
  .slide {
    position: relative;
    width: 1200px;
    height: 676px;
    overflow: hidden;
    background: var(--stage);
    font-family: "Questrial", "Century Gothic", sans-serif;
  }

  /* Section tabs */
  .tab {
    position: absolute;
    top: 4px;
    height: 668px;
    width: 220px;
    border-radius: 16px;
    box-shadow: -3px 0 6px rgba(0,0,0,0.55);
  }
  .tab--green { background: var(--green); }
  .tab--grey { background: var(--grey); }
  .tab--dark { background: var(--grey-dark); }
  .tab-label {
    position: absolute;
    top: 145px;
    height: 382px;
    width: 24px;
    background: var(--label-band);
    border-radius: 0 8px 8px 0;
  }
  .tabs-left .tab-label { left: 0; }
  .tabs-right .tab-label { right: 0; border-radius: 8px 0 0 8px; }
  .tab-label span {
    position: absolute;
    left: 50%;
    top: 50%;
    transform: translate(-50%, -50%) rotate(-90deg);
    white-space: nowrap;
    color: #ffffff;
    font-family: "Montserrat", sans-serif;
    font-weight: 700;
    font-size: 14px;
    letter-spacing: 2.2px;
    text-transform: uppercase;
  }

  /* Main panel */
  .panel {
    position: absolute;
    left: 183px;
    top: 10px;
    width: 920px;
    height: 655px;
    background: var(--paper);
    border-radius: 18px;
    box-shadow: 0 0 10px rgba(0,0,0,0.6);
    z-index: 20;
  }
  .title {
    position: absolute;
    left: 0;
    top: 52px;
    width: 888px;
    margin: 0;
    text-align: center;
    color: var(--green);
    font-family: "Montserrat", sans-serif;
    font-weight: 700;
    font-size: 54px;
    line-height: 1.1;
    letter-spacing: 5px;
  }
  .brand {
    position: absolute;
    right: 40px;
    top: 40px;
    display: flex;
    align-items: center;
    gap: 10px;
  }
  .brand-mark {
    width: 14px;
    height: 14px;
    background: var(--green);
  }
  .brand-name {
    color: var(--brand-grey);
    font-size: 26px;
    line-height: 1;
    letter-spacing: 1px;
  }

  .stat {
    position: absolute;
    top: 170px;
    width: 300px;
    text-align: center;
  }
  .stat--low { left: 72px; }
  .stat--high { left: 508px; }
  .ring {
    position: relative;
    width: 240px;
    height: 240px;
    margin: 0 auto;
  }
  .ring svg { display: block; }
  .ring-value {
    position: absolute;
    inset: 0;
    display: flex;
    align-items: center;
    justify-content: center;
    padding-left: 6px;
    color: var(--green);
    font-family: "Montserrat", sans-serif;
    font-weight: 600;
    font-size: 60px;
    letter-spacing: 6px;
  }
  .stat-text {
    margin: 40px auto 0;
    width: 272px;
    color: var(--ink-soft);
    font-family: "Montserrat", sans-serif;
    font-weight: 600;
    font-size: 14px;
    line-height: 24px;
    letter-spacing: 2.6px;
    text-transform: uppercase;
  }
</style>
</head>
<body>
<div class="slide">

  <nav class="tabs-left" aria-label="Earlier sections">
    <div class="tab tab--green" style="left:0; z-index:1;"><div class="tab-label" style="left:4px;"><span>Roll-out Program</span></div></div>
    <div class="tab tab--dark" style="left:25px; z-index:2;"><div class="tab-label"><span>Community Inolvement</span></div></div>
    <div class="tab tab--grey" style="left:48px; z-index:3;"><div class="tab-label"><span>Case Study</span></div></div>
    <div class="tab tab--green" style="left:72px; z-index:4;"><div class="tab-label"><span>How We Are Different</span></div></div>
    <div class="tab tab--dark" style="left:95px; z-index:5;"><div class="tab-label"><span>Program Overview</span></div></div>
    <div class="tab tab--grey" style="left:118px; z-index:6;"><div class="tab-label"><span>Sample Program</span></div></div>
    <div class="tab tab--green" style="left:141px; z-index:7;"><div class="tab-label" style="left:18px;"><span>Steps to Solution</span></div></div>
  </nav>

  <nav class="tabs-right" aria-label="Later sections">
    <div class="tab tab--green" style="left:978px; z-index:9;"><div class="tab-label" style="right:4px;"><span>A Valuable Partnership</span></div></div>
    <div class="tab tab--dark" style="left:953px; z-index:10;"><div class="tab-label"><span>Our Company</span></div></div>
    <div class="tab tab--grey" style="left:928px; z-index:11;"><div class="tab-label"><span>The Problem</span></div></div>
  </nav>

  <main class="panel">
    <h1 class="title">FACTS</h1>

    <div class="brand">
      <span class="brand-mark" aria-hidden="true"></span>
      <span class="brand-name">Brightar Academy</span>
    </div>

    <section class="stat stat--low">
      <div class="ring">
        <svg width="240" height="240" viewBox="0 0 240 240" aria-hidden="true">
          <circle cx="120" cy="120" r="105" fill="none" stroke="var(--grey)" stroke-width="28"/>
          <circle cx="120" cy="120" r="105" fill="none" stroke="var(--green)" stroke-width="28"
                  stroke-dasharray="14 660" stroke-dashoffset="-510" transform="rotate(-90 120 120)"/>
        </svg>
        <div class="ring-value">2%</div>
      </div>
      <p class="stat-text">Lorem ipsum dolor sit amet, consectetur adi&shy;piscing elit, sed do cus vel facilisis.</p>
    </section>

    <section class="stat stat--high">
      <div class="ring">
        <svg width="240" height="240" viewBox="0 0 240 240" aria-hidden="true">
          <circle cx="120" cy="120" r="105" fill="none" stroke="var(--grey)" stroke-width="28"/>
          <circle cx="120" cy="120" r="105" fill="none" stroke="var(--green)" stroke-width="28"
                  stroke-dasharray="561 660" stroke-dashoffset="-99" transform="rotate(-90 120 120)"/>
        </svg>
        <div class="ring-value">85%</div>
      </div>
      <p class="stat-text">Lorem ipsum dolor sit amet, consectetur adi&shy;piscing elit, sed do eiusmod tempor incidi&shy;dunt ut labore et dolis.</p>
    </section>
  </main>

</div>
</body>
</html>
```